Family Owned Construction Company Needs Modern Business Cards

We need a new design for our business cards. We are a family owned construction company, Brantwell Construction, based in Mendon, Vermont and would like to add in our new logo and find a more modern look. We also want to use our old to make sure people know who we are. We do site development, highway, environmental, demolition, utility and aggregate.

Contact Information for Business Card

We want to have the office address, 418 Quarry Ridge Road, Alder Bend, NX 00418 and our phone (555) 555-0137 and fax (555) 555-0164 on there as well. Our website is www.brantwellinc.example. There should be a place for the person's name, title, cell number, and email address on the card. Words that we would like to be associated with our company are honesty, predictable, reliable, integrity, dedicated, built right quality, consistent, whatever it takes, and innovation. Safety is also very important to us.

Font styles to use
Serif
Sans Serif
Other font styles liked:
• Square 721 Extented

Colors
0255a3
ffffff

Requirements
Must have
• Office address, phone number and fax number. New logo with excavator
Nice to have
• That we do site development, highway, environmental, demolition, utility, and aggregate. Both logos

```html
<!DOCTYPE html>
<html lang="en">
<head>
<meta charset="utf-8">
<title>Brantwell Construction – Business Cards</title>
<link href="https://fonts.googleapis.com/css2?family=Poppins:wght@500;600;700&family=Work+Sans:wght@400&display=swap" rel="stylesheet">
<style>
  :root {
    --navy: #17325f;
    --white: #ffffff;
    --page: #e4e4e4;
    --ink: #1f3563;
    --muted: #4a5570;
  }
  * { box-sizing: border-box; margin: 0; padding: 0; }
  html, body { width: 1200px; height: 1000px; overflow: hidden; }
  body {
    background: var(--page);
    position: relative;
    font-family: "Work Sans", Arial, sans-serif;
  }
  .card {
    position: absolute;
    top: 345px;
    width: 540px;
    height: 310px;
    box-shadow: 0 6px 16px rgba(0,0,0,0.22);
    overflow: hidden;
  }
  .card-front { left: 40px; background: var(--white); }
  .card-back { left: 620px; background: var(--navy); }

  .brand-band {
    position: absolute;
    left: 0; top: 0;
    width: 176px; height: 100%;
    background: var(--navy);
  }
  .band-notch {
    position: absolute;
    left: 176px; top: 14px;
    width: 0; height: 0;
    border-top: 10px solid transparent;
    border-bottom: 10px solid transparent;
    border-left: 12px solid var(--navy);
  }
  .brand-vertical {
    position: absolute;
    left: 88px; top: 155px;
    transform: translate(-50%, -50%) rotate(90deg);
    display: flex; align-items: center; gap: 12px;
    white-space: nowrap;
  }
  .brand-mark {
    width: 22px; height: 22px;
    background: var(--white);
  }
  .brand-name {
    font-family: "Poppins", Arial, sans-serif;
    font-weight: 700;
    color: var(--white);
    line-height: 1;
  }
  .brand-vertical .brand-name { font-size: 25px; }
  .brand-vertical .brand-name small { display: block; font-size: 13px; letter-spacing: 2px; margin-top: 4px; }

  .person {
    position: absolute;
    left: 226px; top: 56px;
  }
  .person-name {
    font-family: "Poppins", Arial, sans-serif;
    font-weight: 600;
    font-size: 20px;
    color: var(--ink);
  }
  .person-title {
    font-family: "Poppins", Arial, sans-serif;
    font-weight: 500;
    font-size: 12px;
    color: var(--ink);
    margin-top: -2px;
  }

  .contact-list {
    position: absolute;
    left: 226px; top: 176px;
    list-style: none;
    font-size: 12.5px;
    color: var(--muted);
  }
  .contact-list li {
    display: flex; align-items: center; gap: 10px;
    height: 19px;
  }
  .contact-list svg { width: 11px; height: 11px; fill: var(--ink); }
  .address {
    position: absolute;
    left: 226px; top: 260px;
    font-size: 12.5px;
    line-height: 17px;
    color: var(--muted);
    font-style: normal;
  }
  .corner-brand {
    position: absolute;
    right: 24px; bottom: 22px;
    display: flex; align-items: center; gap: 8px;
  }
  .corner-brand .brand-mark { width: 34px; height: 34px; background: var(--navy); }
  .corner-brand .brand-name { color: var(--navy); font-size: 13px; }

  .back-brand {
    position: absolute;
    left: 50%; top: 50%;
    transform: translate(-50%, -50%);
    display: flex; align-items: center; gap: 14px;
    white-space: nowrap;
  }
  .back-brand .brand-mark { width: 30px; height: 30px; }
  .back-brand .brand-name { font-size: 34px; }
  .back-brand .brand-name small { display: block; font-size: 15px; letter-spacing: 3px; margin-top: 5px; }
</style>
</head>
<body>

<section class="card card-front" aria-label="Business card front">
  <div class="brand-band">
    <div class="brand-vertical">
      <span class="brand-mark"></span>
      <span class="brand-name">BRANTWELL<small>CONSTRUCTION INC.</small></span>
    </div>
  </div>
  <div class="band-notch"></div>

  <div class="person">
    <p class="person-name">Dorian Vance</p>
    <p class="person-title">Founder</p>
  </div>

  <ul class="contact-list">
    <li>
      <svg viewBox="0 0 16 16"><path d="M3 1h3l1.5 4-2 1.2a9 9 0 0 0 4.3 4.3L11 8.5l4 1.5v3a2 2 0 0 1-2 2A13 13 0 0 1 1 3a2 2 0 0 1 2-2z"/></svg>
      (555) 555-0137
    </li>
    <li>
      <svg viewBox="0 0 16 16"><path d="M4 1h8v4H4z M1 6h14v7h-3v2H4v-2H1z M5 11v3h6v-3z"/></svg>
      (555) 555-0164
    </li>
    <li>
      <svg viewBox="0 0 16 16"><path d="M1 3h14v10H1z M1.5 3.5 8 9l6.5-5.5" stroke="#fff" stroke-width="1.2"/></svg>
      info@dorianvance.example
    </li>
    <li>
      <svg viewBox="0 0 16 16"><circle cx="8" cy="8" r="7"/><path d="M1 8h14M8 1c-3 4-3 10 0 14M8 1c3 4 3 10 0 14" stroke="#fff" stroke-width="1" fill="none"/></svg>
      www.brantwellinc.example
    </li>
  </ul>

  <address class="address">418 Quarry Ridge Road<br>Alder Bend, NX 00418</address>

  <div class="corner-brand">
    <span class="brand-mark"></span>
    <span class="brand-name">BRANTWELL</span>
  </div>
</section>

<section class="card card-back" aria-label="Business card back">
  <div class="back-brand">
    <span class="brand-mark"></span>
    <span class="brand-name">BRANTWELL<small>CONSTRUCTION INC.</small></span>
  </div>
</section>

</body>
</html>
```